Helicopter Company - Skyvane Sweden

I need a new design and implementation of a webpage. We rent helicopters and are also starting a school. We havre started a wordpress but the page is very ugly. Need a complete update. Logo exist already. We also have some pictures of helicotopers. We are open for all designs but it is important that it looks professionel, is eassy to update and will give an impression och structure and dicipline.
Updates

Target Market(s)

Customers that what to get a certificate to fly. It is expensive so it’s either people with a lot of money or people with a big dream. It is very serious business.

Industry/Entity Type

www.skyvane-demo.se

Coding

Coded - Design and coding required

Number of Pages Required

4 page

Font styles to use
Sans Serif

Colors
0054AA
0677BA
7BADD7
CADEEF
E8F1F8

Requirements
Must have
• A easy page the gives a feeling of seriousness and

```html
<!DOCTYPE html>
<html lang="sv">
<head>
<meta charset="utf-8">
<title>Skyvane – Kontakt</title>
<link href="https://fonts.googleapis.com/css2?family=Poppins:wght@300;400;500&display=swap" rel="stylesheet">
<style>
  :root {
    --header-blue: #0876e0;
    --page-bg: #edf2fa;
    --ink-dark: #0c1e55;
    --ink-muted: #a0a6b4;
    --ink-footer: #6e7c9c;
    --field-bg: #ffffff;
    --field-border: #e3e8f0;
    --accent: #ff6430;
    --white: #ffffff;
    --nav-dim: #a9cdf3;
    --divider: #dde3ec;
  }
  * { box-sizing: border-box; margin: 0; padding: 0; }
  html, body { width: 1200px; height: 1096px; overflow: hidden; }
  body {
    position: relative;
    background: var(--page-bg);
    font-family: "Poppins", sans-serif;
    font-weight: 300;
    color: var(--ink-muted);
  }
  .site-header {
    position: absolute; left: 0; top: 0; width: 1200px; height: 76px;
    background: var(--header-blue);
  }
  .brand {
    position: absolute; left: 239px; top: 26px;
    display: flex; align-items: center; gap: 8px;
    color: var(--white); font-weight: 500; font-size: 21px; letter-spacing: 1px;
  }
  .brand-dot { width: 12px; height: 12px; border-radius: 50%; background: var(--white); }
  .main-nav { position: absolute; top: 30px; right: 238px; display: flex; gap: 25px; font-size: 10px; font-weight: 400; }
  .main-nav a { color: var(--nav-dim); text-decoration: none; }
  .main-nav a.is-active { color: var(--white); }

  .intro-photo {
    position: absolute; left: 249px; top: 150px; width: 194px; height: 194px; border-radius: 50%;
    background: linear-gradient(180deg, #2f7cf0 0%, #6fa8ef 25%, #2f5a2a 42%, #6f9a3a 60%, #9fbf50 100%);
  }
  .intro-text { position: absolute; left: 481px; top: 150px; width: 486px; }
  .intro-title { font-weight: 400; font-size: 22.5px; color: var(--ink-dark); line-height: 1.3; }
  .intro-lead { margin-top: 9px; font-weight: 400; font-size: 12.5px; color: var(--ink-dark); }
  .intro-body { margin-top: 9px; font-size: 9.4px; line-height: 16.3px; color: var(--ink-muted); }

  .contact-form { position: absolute; left: 232px; top: 378px; width: 736px; }
  .field {
    display: block; width: 100%; height: 28px; margin-bottom: 18px;
    background: var(--field-bg); border: 1px solid var(--field-border);
    padding: 0 6px; font-family: inherit; font-size: 10px; color: #777;
    line-height: 26px;
  }
  .field-message { height: 138px; padding-top: 5px; line-height: 1.4; margin-bottom: 21px; }
  .send-button {
    display: block; width: 100%; height: 27px; border: 0; border-radius: 2px;
    background: var(--accent); color: var(--white); font-family: inherit; font-size: 10px; font-weight: 400;
  }

  .footer-heading { position: absolute; top: 883px; font-size: 12px; font-weight: 400; color: var(--ink-footer); }
  .links-heading { left: 226px; }
  .hours-heading { left: 481px; }
  .contact-heading { right: 226px; }
  .link-list { position: absolute; left: 234px; top: 927px; list-style: none; font-size: 9.6px; }
  .link-list li { display: flex; align-items: center; gap: 8px; height: 22.5px; }
  .link-list a { color: var(--ink-muted); text-decoration: none; }
  .hours-text { position: absolute; left: 481px; top: 907px; width: 240px; font-size: 9.6px; line-height: 16.3px; }
  .contact-details { position: absolute; right: 276px; top: 907px; text-align: right; font-size: 9.6px; line-height: 16.3px; }
  .contact-icon { position: absolute; left: 947px; top: 920px; }

  .footer-divider { position: absolute; left: 0; top: 1039px; width: 1200px; height: 1px; background: var(--divider); }
  .copyright { position: absolute; left: 226px; top: 1059px; font-size: 9.6px; }
  .back-to-top { position: absolute; left: 954px; top: 1062px; }
</style>
</head>
<body>
  <header class="site-header">
    <div class="brand"><span class="brand-dot"></span>SKYVANE</div>
    <nav class="main-nav">
      <a href="#">Start</a>
      <a href="#" class="is-active">Kontakt</a>
    </nav>
  </header>

  <div class="intro-photo" role="img" aria-label="Helikoptrar parkerade på en gräsplan framför skog under blå himmel"></div>
  <section class="intro-text">
    <h1 class="intro-title">Vill du hyra helikopter av oss?</h1>
    <p class="intro-lead">Ring oss eller skicka ett mail så återkommer vi så snart som möjligt.</p>
    <p class="intro-body">Skriv ner när du vill hyra, hur mycket du har flugit och vilka dina behörigheter är. Undrar du något annat är du välkommen att skriva med den frågan direkt. Vill du ha hjälp med något annat gällande flygning. Exempelvis invetering från Helikopter i Norrby kan du även fråga det här.</p>
  </section>

  <form class="contact-form">
    <div class="field">Your name</div>
    <div class="field">Your e-mail</div>
    <div class="field">Subject</div>
    <div class="field field-message">Message</div>
    <button type="button" class="send-button">Send a message</button>
  </form>

  <h2 class="footer-heading links-heading">Länkar</h2>
  <ul class="link-list">
    <li><svg width="8" height="8" viewBox="0 0 8 8"><path d="M0 4h7M4 1l3 3-3 3" fill="none" stroke="#ff6430" stroke-width="1"/></svg><a href="#">www.rotorpad-demo.se</a></li>
    <li><svg width="8" height="8" viewBox="0 0 8 8"><path d="M0 4h7M4 1l3 3-3 3" fill="none" stroke="#ff6430" stroke-width="1"/></svg><a href="#">www.aerolift-demo.com</a></li>
    <li><svg width="8" height="8" viewBox="0 0 8 8"><path d="M0 4h7M4 1l3 3-3 3" fill="none" stroke="#ff6430" stroke-width="1"/></svg><a href="#">www.norrbyflygklubb-demo.se</a></li>
  </ul>

  <h2 class="footer-heading hours-heading">Öppetider</h2>
  <p class="hours-text">Måndag – Söndag: 0900 – 1700 Övrig tid enligt överenskommelse.</p>

  <h2 class="footer-heading contact-heading">Kontaktinformation</h2>
  <p class="contact-details">Skyvane, Norrby Flygfält,<br>+46 (0) 700 123 456<br>info@skyvane-demo.se</p>
  <svg class="contact-icon" width="27" height="27" viewBox="0 0 27 27" fill="none" stroke="#ff6430" stroke-width="1.4" stroke-linecap="round">
    <path d="M6 14c-3 3-3 5-1 7l1 1c2 2 4 2 7-1l9-9c3-3 3-5 1-7l-1-1c-1-1-2-1-3 0l-2 2c-1 1-1 2 0 3l1 1-7 7-1-1c-1-1-2-1-3 0z"/>
    <path d="M16 2c4 0 8 3 9 8M16 6c2 0 4 2 5 4"/>
  </svg>

  <div class="footer-divider"></div>
  <p class="copyright">© 2022 - Skyvane | All Rights Reserved</p>
  <svg class="back-to-top" width="14" height="8" viewBox="0 0 14 8"><path d="M1 7l6-6 6 6" fill="none" stroke="#6e7c9c" stroke-width="1.2"/></svg>
</body>
</html>
```